Renaldo's Motorworks landing page to Dealership page, Rental Car Page, and Auto Body page.

I'm looking for my website to have RenaldosMotor.com be the landing page. From there visitors will have the option to visit three pages. My auto dealer page, of which I will provide an example of how I'd like it done. Auto body page, where I will fill in the text. The rental car page. Basically on the auto dealer and rental page I'll need the ability to add vehicles and delete as I need. Otherwise, its a pretty straightforward site. Nothing extensive. I already have the logo design from a previous project on here completed and can provide. If more funded needed for page capabilities, I can provide. I do have an account with HostPeak, with renaldosmotor.com already under them.

Target Market(s)

Automotive

Industry/Entity Type

Auto body repair, dealership, rental car.

Coding

Coded - Design and coding required

Number of Pages Required

4 page

Font styles to use
Sans Serif

Colors
0054AA
0677BA
7BADD7
CADEEF
E8F1F8

Requirements
Must have
• My logo Renaldos Motorworks at the top. Be creative with pics in the background of cars.
Nice to have
• Ease of use with being able to add vehicles for sale, and rental cars.
Should not have
• Nothing complex, would like to get in and out. Nothing to extensive on the designs of the pages, simple but attractive.

```html
<!DOCTYPE html>
<html lang="en">
<head>
<meta charset="utf-8">
<title>Renaldo's Motorworks – Landing Page</title>
<link href="https://fonts.googleapis.com/css2?family=Bebas+Neue&family=Lato:wght@400;700;900&display=swap" rel="stylesheet">
<style>
  :root{
    --blue-deep:#0054AA;
    --blue-mid:#0677BA;
    --blue-soft:#7BADD7;
    --blue-pale:#CADEEF;
    --blue-mist:#E8F1F8;
    --ink:#1b1f26;
    --white:#ffffff;
    --dark-btn:#1c1c1c;
  }
  *{box-sizing:border-box;margin:0;padding:0}
  html,body{width:884px;height:1200px;overflow:hidden}
  body{background:var(--blue-pale);font-family:'Lato',sans-serif;position:relative;color:var(--ink)}

  /* brand block */
  .brand{position:absolute;top:150px;left:0;width:884px;text-align:center}
  .brand-name{font-family:'Lato',sans-serif;font-weight:900;font-size:46px;color:var(--ink);letter-spacing:1px;display:inline-flex;align-items:center;gap:14px}
  .brand-dot{width:18px;height:18px;border-radius:50%;background:var(--blue-mid);display:inline-block}

  /* side labels */
  .side-label{position:absolute;font-family:'Lato',sans-serif;font-size:11px;letter-spacing:7px;color:var(--blue-mid);transform:rotate(-90deg);transform-origin:left top;white-space:nowrap}
  .side-label.desktop{left:18px;top:800px}
  .side-label.mobile{left:700px;top:880px}

  /* desktop page */
  .page-desktop{position:absolute;left:40px;top:330px;width:620px;height:472px;background:var(--white);overflow:hidden;box-shadow:0 6px 24px rgba(0,84,170,.15)}
  .topbar{height:19px;background:var(--blue-deep);display:flex;align-items:center;color:var(--white);font-size:6px;padding:0 80px}
  .topbar .contact{display:flex;gap:14px;flex:1}
  .topbar .socials{display:flex;gap:4px}
  .social{width:10px;height:10px;background:var(--blue-mid);display:block}
  .social.on{background:var(--white)}
  .site-header{height:57px;display:flex;align-items:center;justify-content:center}
  .site-logo{font-weight:900;font-size:16px;color:var(--ink);display:flex;align-items:center;gap:6px}
  .site-logo .brand-dot{width:8px;height:8px}
  .hero{position:absolute;left:0;top:76px;width:620px;height:320px}
  .hero svg{position:absolute;inset:0}
  .car-photo{position:absolute;left:80px;top:55px;width:240px;height:150px;border-radius:40% 45% 30% 30%;background:radial-gradient(ellipse at 50% 55%,#2f8fe0 0%,#1466c2 55%,rgba(20,102,194,0) 72%)}
  .hero-copy{position:absolute;left:335px;top:90px;width:260px;color:var(--white)}
  .eyebrow{font-size:6px;letter-spacing:2.4px;display:flex;align-items:center;gap:6px}
  .eyebrow::before,.eyebrow::after{content:"";width:22px;height:1px;background:var(--blue-soft)}
  .hero-title{font-family:'Bebas Neue',sans-serif;font-size:29px;line-height:28px;margin-top:6px;letter-spacing:.5px}
  .hero-text{font-size:6.5px;line-height:11px;margin-top:8px}
  .services{position:absolute;left:84px;top:365px;width:452px;height:120px;background:var(--white);padding:5px;display:flex;gap:5px;box-shadow:0 2px 8px rgba(0,0,0,.08)}
  .service{flex:1;display:flex;flex-direction:column}
  .service-photo{height:77px}
  .service-btn{height:35px;display:flex;align-items:center;justify-content:center;color:var(--white);font-size:7px;font-weight:700;letter-spacing:.3px}
  .service-btn.blue{background:var(--blue-deep)}
  .service-btn.dark{background:var(--dark-btn)}
  .photo-deal{background:linear-gradient(135deg,#c9d6e2,#5f6e80)}
  .photo-body{background:linear-gradient(135deg,#8aa2bb,#2d3a4a)}
  .photo-rent{background:linear-gradient(135deg,#e6edf3,#4a5563)}

  /* mobile page */
  .page-mobile{position:absolute;left:714px;top:330px;width:130px;height:536px;background:var(--white);overflow:hidden;box-shadow:0 6px 24px rgba(0,84,170,.15)}
  .m-topbar{height:11px;background:var(--blue-deep);color:var(--white);font-size:3px;display:flex;align-items:center;gap:6px;padding:0 8px}
  .m-header{height:39px;display:flex;align-items:center;justify-content:space-between;padding:0 10px}
  .m-logo{font-weight:900;font-size:9px;color:var(--ink);display:flex;align-items:center;gap:3px}
  .m-logo .brand-dot{width:5px;height:5px}
  .burger{width:8px;height:5px;border-top:1px solid var(--blue-soft);border-bottom:1px solid var(--blue-soft);position:relative}
  .burger::after{content:"";position:absolute;left:0;right:0;top:1px;height:1px;background:var(--blue-soft)}
  .m-hero{position:absolute;top:50px;left:0;width:130px;height:365px}
  .m-hero svg{position:absolute;inset:0}
  .m-copy{position:absolute;top:38px;left:0;width:130px;text-align:center;color:var(--blue-soft)}
  .m-eyebrow{font-size:3.5px;letter-spacing:1px}
  .m-title{font-family:'Bebas Neue',sans-serif;font-size:13px;line-height:13px;margin-top:3px}
  .m-car{position:absolute;left:6px;top:106px;width:118px;height:60px;border-radius:40% 45% 30% 30%;background:radial-gradient(ellipse at 50% 55%,#2f8fe0 0%,#1466c2 55%,rgba(20,102,194,0) 72%)}
  .m-services{position:absolute;left:12px;top:262px;width:106px;background:var(--white);padding:3px;display:flex;flex-direction:column;gap:4px;box-shadow:0 1px 5px rgba(0,0,0,.08)}
  .m-service-photo{height:58px}
  .m-service-btn{height:20px;display:flex;align-items:center;justify-content:center;color:var(--white);font-size:4px;font-weight:700}
  .m-service-btn.blue{background:var(--blue-deep)}
  .m-service-btn.dark{background:var(--dark-btn)}
</style>
</head>
<body>

<div class="brand">
  <span class="brand-name"><span class="brand-dot"></span>Renaldo's Motorworks</span>
</div>

<div class="side-label desktop">DESKTOP / LAPTOP</div>
<div class="side-label mobile">RESPONSIVE SIDE</div>

<section class="page-desktop">
  <div class="topbar">
    <div class="contact">
      <span>&#9742; +1 234 567 890</span>
      <span>&#9993; info@renaldosmotorworks.com</span>
    </div>
    <div class="socials">
      <span class="social"></span><span class="social on"></span><span class="social"></span>
    </div>
  </div>
  <header class="site-header">
    <div class="site-logo"><span class="brand-dot"></span>Renaldo's Motorworks</div>
  </header>
  <div class="hero">
    <svg width="620" height="320" viewBox="0 0 620 320">
      <defs>
        <linearGradient id="heroBlue" x1="0" y1="0" x2="1" y2="1">
          <stop offset="0" stop-color="#0677BA"/>
          <stop offset="1" stop-color="#0a6bb5"/>
        </linearGradient>
      </defs>
      <rect width="620" height="320" fill="#E8F1F8"/>
      <polygon points="370,0 620,0 620,218 260,320 250,320" fill="url(#heroBlue)"/>
      <polygon points="620,218 620,320 250,320" fill="#E8F1F8"/>
      <line x1="364" y1="0" x2="246" y2="320" stroke="#0677BA" stroke-width="1.5"/>
    </svg>
    <div class="car-photo" role="img" aria-label="Blue sports coupe, front three-quarter view"></div>
    <div class="hero-copy">
      <div class="eyebrow">WELCOME TO RENALDO'S MOTORWORKS</div>
      <h1 class="hero-title">Your partner in auto<br>dealing &amp; rental</h1>
      <p class="hero-text">Lorem ipsum dolor sit amet consectetur adipiscing elit. Utelit tellus tet luctus ertnecari ullamcorper mattis pulvinar dapibus leo consectetur.</p>
    </div>
  </div>
  <div class="services">
    <div class="service">
      <div class="service-photo photo-deal" role="img" aria-label="Dealer shaking hands with a customer beside a car"></div>
      <a class="service-btn blue">AUTO DEALER &rarr;</a>
    </div>
    <div class="service">
      <div class="service-photo photo-body" role="img" aria-label="Mechanic working under an open car hood"></div>
      <a class="service-btn dark">AUTO BODY &rarr;</a>
    </div>
    <div class="service">
      <div class="service-photo photo-rent" role="img" aria-label="Hand opening the door of a rental car"></div>
      <a class="service-btn blue">RENTAL CAR &rarr;</a>
    </div>
  </div>
</section>

<section class="page-mobile">
  <div class="m-topbar"><span>+1 234 567 890</span><span>info@renaldosmotorworks.com</span></div>
  <header class="m-header">
    <div class="m-logo"><span class="brand-dot"></span>Renaldo's</div>
    <span class="burger"></span>
  </header>
  <div class="m-hero">
    <svg width="130" height="365" viewBox="0 0 130 365">
      <rect width="130" height="365" fill="#E8F1F8"/>
      <polygon points="130,0 130,365 20,365 20,350" fill="#0054AA"/>
      <polygon points="130,0 130,60 78,172 40,300" fill="#0677BA" opacity=".0"/>
    </svg>
    <div class="m-copy">
      <div class="m-eyebrow">— WELCOME TO RENALDO'S MOTORWORKS —</div>
      <div class="m-title">Your partner in auto<br>dealing &amp; rental</div>
    </div>
    <div class="m-car" role="img" aria-label="Blue sports coupe, front three-quarter view"></div>
  </div>
  <div class="m-services">
    <div class="m-service-photo photo-deal" role="img" aria-label="Dealer shaking hands with a customer"></div>
    <a class="m-service-btn blue">AUTO DEALER &rarr;</a>
    <div class="m-service-photo photo-body" role="img" aria-label="Mechanic working under a car hood"></div>
    <a class="m-service-btn dark">AUTO BODY &rarr;</a>
    <div class="m-service-photo photo-rent" role="img" aria-label="Hand opening a rental car door"></div>
    <a class="m-service-btn blue">RENTAL CAR &rarr;</a>
  </div>
</section>

</body>
</html>
```